Visitenkarten für Familienunternehmen in den Bereichen Fliesen, Natursteine, Kaminöfen, Schwimmbäder und Whirlpools
Zielgruppe
Wir sind ein Familienunternehmen in dritter Generation und Spezialist für Fliesen, Natursteine, Kaminöfen, Schwimmbäder und Whirlpools. Professionell, kreativ und voller Leidenschaft begleiten wir unsere Kunden bei der Umsetzung ihrer Vorhaben. Von der persönlichen Beratung bis hin zur Ausführung profitieren unsere Kunden von qualifiziertem Fachpersonal und 60 Jahren Erfahrung. Unsere Zielgruppe sind Familien/Paare ab 35 Jahren, die Produkte höchster Qualität für Ihr Zuhause suchen.
Aufgabenstellung
Wir benötigen neue Visitenkarten, da wir ein neues Logo haben. Wir haben folgende Vorstellung:
Rückseite: Komplett schwarz bzw. dunkel (Farbton ähnlich DB703), mittig unser neues Logo in weiß.
Vorderseite: Auch hier Hintergrund schwarz, Logo in weiß, Name des Ansprechpartners samt Titel/Position, Firmenname, Adresse, Telefonnummer, eMail-Adresse und Social Media-Adresse. Des Weiteren sollte unser Portfolio aufgelistet sein (Fliesen, Natursteine, Kaminöfen, Schwimmbäder und Whirlpools). Alternativ können wir uns die Auflistung des Portfolios auch auf der Rückseite vorstellen. Alternativ können wir uns die Vorderseite auch in weiß mit schwarzer Schrift vorstellen.
Der Inhalt der Datei, welche am Ende erstellt wird, muss für unsere Druckerei editierbar sein (Schrift als Text, nicht als Pfad).
Ergänzung 25.03.2023:
Nachdem die ersten Design-Vorschläge eingetroffen sind, haben wir uns dazu entschieden, dass es eine Visitenkarte im Querformat sein soll. Vorder- und Rückseite vollen schwarz/dunkel sein.

```html
<!DOCTYPE html>
<html lang="de">
<head>
<meta charset="utf-8">
<title>Steinhaus Perl – Visitenkarte</title>
<link rel="stylesheet" href="https://fonts.googleapis.com/css2?family=DM+Sans:wght@300;400;700&display=swap">
<style>
  :root {
    --stage: #b0916a;
    --card: #3a3635;
    --ink: #ffffff;
    --gold: #c9a26c;
    --rule: #9a8062;
  }
  * { margin: 0; padding: 0; box-sizing: border-box; }
  html, body { width: 1200px; height: 846px; overflow: hidden; }
  body {
    position: relative;
    background: var(--stage);
    font-family: "DM Sans", Arial, sans-serif;
    color: var(--ink);
  }
  .card {
    position: absolute;
    background: var(--card);
  }
  .card--back { left: 246px; top: 83px; width: 486px; height: 314px; }
  .card--front { left: 550px; top: 437px; width: 490px; height: 316px; }

  .brand-name {
    position: absolute;
    font-weight: 300;
    color: var(--ink);
    white-space: nowrap;
    line-height: 1;
  }
  .card--back .brand-name {
    left: 0; right: 0; top: 120px;
    text-align: center;
    font-size: 50px;
    letter-spacing: 0.32em;
    padding-left: 0.32em;
  }
  .card--front .brand-name {
    left: 279px; top: 44px; width: 166px;
    text-align: center;
    font-size: 30px;
    letter-spacing: 0.3em;
    padding-left: 0.3em;
  }

  .company {
    position: absolute;
    left: 44px; top: 58px;
    font-size: 14px; font-weight: 700;
    letter-spacing: 0.02em;
    color: var(--gold);
  }
  .company-rule {
    position: absolute;
    left: 44px; top: 80px;
    width: 222px; height: 1.5px;
    background: var(--rule);
  }

  .contact-person {
    position: absolute;
    left: 44px; top: 121px;
    font-size: 15px; line-height: 22px;
  }
  .contact-person .name { font-weight: 700; }
  .contact-person .role { font-weight: 300; }

  .contact-details {
    position: absolute;
    left: 212px; top: 121px;
    font-size: 15px; line-height: 22px;
  }
  .contact-details p { white-space: nowrap; }
  .contact-details .group + .group { margin-top: 12px; }
  .social { display: flex; align-items: center; gap: 8px; }
  .social svg { flex: none; }

  .portfolio {
    position: absolute;
    left: 44px; top: 282px;
    font-size: 14px;
    color: var(--gold);
    white-space: nowrap;
  }
</style>
</head>
<body>
  <section class="card card--back" aria-label="Rückseite">
    <div class="brand-name">PERL</div>
  </section>

  <section class="card card--front" aria-label="Vorderseite">
    <div class="company">STEINHAUS PERL GMBH</div>
    <div class="company-rule"></div>
    <div class="brand-name">PERL</div>

    <div class="contact-person">
      <p class="name">Timo Perl</p>
      <p class="role">Geschäftsführer</p>
    </div>

    <div class="contact-details">
      <div class="group">
        <p>Lindenweg 12 | 76829 Talheim</p>
        <p>Tel.: +49 (0) 06 12 3 - 45 67 00</p>
      </div>
      <div class="group">
        <p>Mail: info@steinhaus-perl.de</p>
        <p>Web: www.steinhaus-perl.de</p>
        <p class="social">
          <svg width="12" height="12" viewBox="0 0 12 12" aria-hidden="true"><circle cx="6" cy="6" r="5" fill="none" stroke="#ffffff" stroke-width="1.4"/></svg>
          <span>@steinhausperl</span>
        </p>
      </div>
    </div>

    <div class="portfolio">Fliesen | Natursteine | Kaminöfen | Schwimmbäder | Whirlpools</div>
  </section>
</body>
</html>
```